Lime Wash Direct Mail Postcard Design

I need a postcard that is going to be mailed.
We are a residential and commerical painting company. We are going to start marking our Ventian Plaster, Lime Wash, Roman Clay, Mineral Wash.
I've attached the layout to use that shows bleed and such. I've included a mock up I've done to get an idea of what I want.
- I want it to look sophicated
- Speciality
- Art
I've included logos of 2 companies - Velastra and Cindrel to show.
I want to show mostly interior work but one or 2 lime wash houses that's lighter, shows the bricks in area would be good.
I love the saying "You're unique - Your Home Should Be Too" or if you have a better variation of that, I'd be open to it.

```html
<!DOCTYPE html>
<html lang="en">
<head>
<meta charset="utf-8">
<title>Fairmont Finishes – Postcard</title>
<link rel="stylesheet" href="https://fonts.googleapis.com/css2?family=Tinos:wght@400;700&display=swap">
<style>
  :root {
    --page-bg: #eeeeee;
    --card-white: #ffffff;
    --brand-blue: #2196d6;
    --ink: #151515;
    --ink-soft: #3a3a3a;
    --gold: #c4924a;
    --gold-light: #e2c48f;
    --sand: #e9d3a8;
    --brush-grey: #8a8d91;
    --wall-1: #bfc0be;
    --wall-2: #dcd8cf;
    --wall-3: #e0d9c8;
    --wall-4: #e6e8e8;
  }
  * { margin: 0; padding: 0; box-sizing: border-box; }
  html, body {
    width: 1200px; height: 900px; overflow: hidden;
    background: var(--page-bg);
    font-family: "Tinos", "Times New Roman", serif;
  }
  .postcard {
    position: absolute; left: 40px; top: 53px;
    width: 1120px; height: 794px;
    background: var(--card-white);
    overflow: hidden;
    box-shadow: 0 2px 10px rgba(0,0,0,.12);
  }
  .postcard-art { position: absolute; inset: 0; }
  .brand-name {
    position: absolute; left: 113px; top: 62px;
    font-size: 30px; font-weight: 700; letter-spacing: .5px;
    color: var(--ink);
  }
  .headline {
    position: absolute; left: 107px; top: 395px;
    font-size: 61px; line-height: 73px; font-weight: 400;
    color: var(--ink); letter-spacing: -0.5px;
  }
  .headline strong { font-weight: 700; }
  .offer {
    position: absolute; left: 791px; top: 367px; width: 248px; height: 248px;
    text-align: center; color: var(--ink-soft);
  }
  .offer-date { margin-top: 58px; font-size: 34px; }
  .offer-deal { margin-top: 6px; font-size: 40px; font-weight: 700; letter-spacing: 3px; line-height: 40px; }
  .offer-note { font-size: 13px; font-weight: 700; letter-spacing: 1.5px; }
  .contact {
    position: absolute; right: 36px; top: 660px; text-align: right; color: var(--ink-soft);
  }
  .contact-phone { font-size: 28px; font-weight: 700; letter-spacing: 4px; }
  .contact-email { font-size: 15px; letter-spacing: 3px; margin-top: 2px; }
  .website {
    position: absolute; left: 130px; top: 752px;
    font-size: 16px; font-weight: 700; letter-spacing: 11px; color: var(--ink);
  }
  .partners {
    position: absolute; right: 36px; top: 730px;
    display: flex; align-items: center; gap: 18px;
  }
  .partner-cindrel { font-size: 32px; letter-spacing: 3px; color: var(--sand); }
  .partner-divider { width: 1px; height: 56px; background: var(--ink-soft); }
  .partner-velastra { font-size: 34px; font-weight: 700; color: var(--ink); }
</style>
</head>
<body>
  <main class="postcard">
    <svg class="postcard-art" width="1120" height="794" viewBox="0 0 1120 794">
      <defs>
        <linearGradient id="wall-tones" x1="0" x2="1" y1="0" y2="0">
          <stop offset="0" stop-color="var(--wall-1)"/>
          <stop offset=".3" stop-color="var(--wall-2)"/>
          <stop offset=".6" stop-color="var(--wall-3)"/>
          <stop offset=".85" stop-color="var(--wall-4)"/>
        </linearGradient>
        <radialGradient id="gold-disc" cx=".5" cy=".5" r=".5">
          <stop offset=".8" stop-color="var(--gold)"/>
          <stop offset="1" stop-color="var(--gold-light)"/>
        </radialGradient>
      </defs>
      <rect class="wall-photo" role="img" aria-label="Interior walls finished in Venetian plaster and lime wash beside a white brick wall" x="0" y="0" width="1120" height="794" fill="url(#wall-tones)"/>
      <path class="brand-band-edge" d="M0 0 H800 L760 20 C600 60 480 200 250 225 C150 235 60 240 0 236 Z" fill="var(--brush-grey)" opacity=".7"/>
      <path class="brand-band" d="M0 0 H790 C600 30 470 180 250 212 C150 224 60 224 0 218 Z" fill="var(--brand-blue)"/>
      <path class="base-wave-edge" d="M0 590 C150 700 420 720 700 640 C850 600 1000 440 1120 380 V794 H0 Z" fill="var(--brush-grey)" opacity=".75"/>
      <path class="base-wave" d="M0 610 C160 712 420 735 700 660 C860 615 1010 460 1120 410 V794 H0 Z" fill="var(--card-white)"/>
      <circle class="offer-ring" cx="915" cy="491" r="132" fill="none" stroke="var(--gold-light)" stroke-width="4" opacity=".8"/>
      <circle class="offer-disc" cx="915" cy="491" r="124" fill="url(#gold-disc)"/>
    </svg>

    <div class="brand-name">Fairmont Finishes</div>

    <h1 class="headline"><strong>YOU'RE UNIQUE</strong><br>YOUR <strong>HOME SHOULD</strong><br>BE TOO</h1>

    <div class="offer">
      <div class="offer-date">31 JAN</div>
      <div class="offer-deal">10% OFF</div>
      <div class="offer-note">FREE CONSULTATION</div>
    </div>

    <div class="contact">
      <div class="contact-phone">555-014-2290</div>
      <div class="contact-email">OFFICE@FAIRMONTFINISH.COM</div>
    </div>

    <div class="website">WWW.FAIRMONTFINISH.COM</div>

    <div class="partners">
      <span class="partner-cindrel">CINDREL</span>
      <span class="partner-divider"></span>
      <span class="partner-velastra">VELASTRA</span>
    </div>
  </main>
</body>
</html>
```